QRV Law Letterhead

Want law firm letterhead - both in terms of a pdf file that I can use electronically as letterhead by adding it as a background - and in terms of a file that I can send to a company to create actual letterhead.
Industry/Entity Type
Law Firm
Font styles to use
Sans Serif
Requirements
Must have
- Should have the following information (you can decide where to place):
- My name - Corwin Haldane
- My email - corwin@qrvlawfirm.example
- My address - 2816 Pellworth Parkway 317-842
- San Jose, California 95742
- Website - www.qrvlawfirm.example
- Phone - 408-555-0187
- Fax - 408-555-0243
- The logo I attached
Nice to have
- I think I would prefer to have a black and white color scheme.
- I don't necessarily need a title after my name, but I have seen a few design submissions that include a generic title. The title I would use is "IP Litigator & Trademark Attorney"

```html
<!DOCTYPE html>
<html lang="en">
<head>
<meta charset="utf-8">
<title>QRV Law Letterhead</title>
<link href="https://fonts.googleapis.com/css2?family=Roboto:wght@400;500;700&display=swap" rel="stylesheet">
<style>
  :root {
    --backdrop: #c9c5c9;
    --paper: #ffffff;
    --ink: #111111;
    --band: #000000;
    --band-inner: #0c0c0c;
    --faint: #d3d3d3;
    --band-text: #e8e8e8;
  }
  * { margin: 0; padding: 0; box-sizing: border-box; }
  html, body { width: 1200px; height: 1200px; overflow: hidden; }
  body {
    background: var(--backdrop);
    font-family: "Roboto", Arial, sans-serif;
    color: var(--ink);
    position: relative;
  }
  .letterhead {
    position: absolute;
    left: 293px; top: 198px;
    width: 616px; height: 795px;
    background: var(--paper);
  }
  .brand {
    position: absolute;
    left: 25px; top: 20px;
    display: flex; align-items: center; gap: 9px;
  }
  .brand-mark {
    width: 46px; height: 46px;
    border: 6px solid var(--ink);
    border-radius: 50%;
  }
  .brand-name {
    font-size: 34px;
    font-weight: 500;
    letter-spacing: 0.5px;
    line-height: 1;
  }
  .contact {
    position: absolute;
    left: 473px; top: 26px;
    list-style: none;
    font-size: 8.5px;
    font-weight: 700;
    line-height: 10.3px;
  }
  .contact li { display: flex; align-items: center; gap: 5px; }
  .contact svg { width: 8px; height: 8px; flex: none; }
  .watermark {
    position: absolute;
    left: 137px; top: 250px;
    width: 320px; height: 300px;
    display: flex; align-items: center; justify-content: center;
    font-size: 86px;
    font-weight: 700;
    color: var(--faint);
    letter-spacing: 2px;
  }
  .signatory {
    position: absolute;
    left: 62px; top: 676px;
    font-size: 10.5px;
    font-weight: 700;
    text-transform: uppercase;
    letter-spacing: 0.2px;
  }
  .footer-band {
    position: absolute;
    left: 0; bottom: 0;
    width: 100%; height: 43px;
    background: var(--band);
  }
  .footer-address {
    position: absolute;
    left: 128px; top: 0;
    width: 352px; height: 100%;
    background: var(--band-inner);
    display: flex; align-items: center;
    padding-left: 30px; gap: 8px;
    color: var(--band-text);
    font-size: 8.5px;
    font-weight: 500;
  }
  .footer-address svg { width: 12px; height: 12px; flex: none; }
</style>
</head>
<body>
  <main class="letterhead">
    <header class="brand">
      <span class="brand-mark" aria-hidden="true"></span>
      <span class="brand-name">QRV Law</span>
    </header>

    <ul class="contact">
      <li>
        <svg viewBox="0 0 10 10"><circle cx="5" cy="5" r="5" fill="#111"/><path d="M3.3 2.6l1 1-.6.7a4 4 0 0 0 2 2l.7-.6 1 1-.8.8c-2 0-4-2-4-4z" fill="#fff"/></svg>
        408-555-0187
      </li>
      <li>
        <svg viewBox="0 0 10 10"><rect x="2.5" y="1" width="5" height="3" fill="#111"/><rect x="1" y="3.5" width="8" height="4" rx="1" fill="#111"/><rect x="3" y="6" width="4" height="3.5" fill="#111" stroke="#fff" stroke-width=".6"/></svg>
        408-555-0243
      </li>
      <li>
        <svg viewBox="0 0 10 10"><circle cx="5" cy="5" r="5" fill="#111"/><rect x="2.5" y="3.2" width="5" height="3.6" fill="none" stroke="#fff" stroke-width=".8"/><path d="M2.5 3.3L5 5.2l2.5-1.9" fill="none" stroke="#fff" stroke-width=".8"/></svg>
        corwin@qrvlawfirm.example
      </li>
      <li>
        <svg viewBox="0 0 10 10"><circle cx="5" cy="5" r="5" fill="#111"/><circle cx="5" cy="5" r="2.8" fill="none" stroke="#fff" stroke-width=".7"/><path d="M2.2 5h5.6M5 2.2v5.6" stroke="#fff" stroke-width=".6"/></svg>
        www.qrvlawfirm.example
      </li>
    </ul>

    <div class="watermark" aria-hidden="true">QRV</div>

    <p class="signatory">Corwin Haldane</p>

    <footer class="footer-band">
      <div class="footer-address">
        <svg viewBox="0 0 12 12"><path d="M6 .8a4 4 0 0 0-4 4c0 3 4 6.6 4 6.6s4-3.6 4-6.6a4 4 0 0 0-4-4z" fill="#fff"/><circle cx="6" cy="4.8" r="1.5" fill="#0c0c0c"/></svg>
        <span>2816 Pellworth Parkway 317-842, &nbsp;San Jose, California 95742</span>
      </div>
    </footer>
  </main>
</body>
</html>
```